Business Card Design

We have recently seen two business cards that caught our attention and think the designs would work for us. We are an accounting firm that serves small businesses in a variety of industries. Attached are the two business card that inspired us along with very rough layouts. We would like to see a professional layout using our company information.

Industry/Entity Type

Accounting

Contact Information for Business Card

Company Name - Dalworth Pryce
Address - 4180 Brambleton Lane, Suite 310, Houston, TX 77051
713-508-9627 - Main
281-369-0714 - Fax

Team Member Names, emails and phone numbers (see attachment)

```html
<!DOCTYPE html>
<html lang="en">
<head>
<meta charset="utf-8">
<title>Dalworth Pryce — Business Cards</title>
<link rel="stylesheet" href="https://fonts.googleapis.com/css2?family=Cinzel:wght@600&family=Open+Sans:wght@400;600;700&display=swap">
<style>
  :root {
    --backdrop: #e4e4e2;
    --card-white: #f7f7f7;
    --charcoal: #333335;
    --swoosh-grey: #a9a9ab;
    --swoosh-light: #d3d3d4;
    --brand-ink: #2e2e30;
    --on-dark: #ffffff;
    --on-dark-soft: #d6d6d6;
  }
  html, body {
    margin: 0;
    width: 1200px;
    height: 901px;
    overflow: hidden;
    background: var(--backdrop);
  }
  .sheet {
    position: relative;
    width: 1200px;
    height: 901px;
  }
  .card {
    position: absolute;
    left: 260px;
    width: 680px;
    height: 389px;
    border-radius: 30px;
    overflow: hidden;
    background: var(--card-white);
    box-shadow: 0 6px 18px rgba(0,0,0,0.18);
  }
  .card--front { top: 41px; }
  .card--back { top: 471px; }
  .card svg.card-art {
    position: absolute;
    inset: 0;
    width: 100%;
    height: 100%;
  }
  .brand {
    position: absolute;
    font-family: "Cinzel", serif;
    font-weight: 600;
    font-size: 34px;
    color: var(--brand-ink);
    letter-spacing: 2px;
    display: flex;
    align-items: center;
    gap: 12px;
    white-space: nowrap;
  }
  .brand-mark {
    width: 14px;
    height: 14px;
    border-radius: 50%;
    background: var(--brand-ink);
  }
  .card--front .brand { left: 56px; top: 92px; }
  .card--back .brand { left: 232px; top: 112px; }

  .person {
    position: absolute;
    left: 36px;
    bottom: 26px;
    font-family: "Open Sans", sans-serif;
    color: var(--on-dark);
  }
  .person-name { font-size: 19px; font-weight: 700; margin: 0; }
  .person-title { font-size: 14px; font-weight: 400; margin: 2px 0 0; color: var(--on-dark-soft); }

  .contact {
    position: absolute;
    right: 26px;
    bottom: 22px;
    margin: 0;
    padding: 0;
    list-style: none;
    font-family: "Open Sans", sans-serif;
    font-size: 11px;
    line-height: 15px;
    color: var(--on-dark);
    text-align: right;
  }
  .contact li {
    display: flex;
    justify-content: flex-end;
    align-items: center;
    gap: 7px;
  }
  .contact .icon {
    width: 8px;
    height: 8px;
    border-radius: 50%;
    background: var(--on-dark);
    flex: none;
  }
  .contact .icon--blank { background: transparent; }
  .contact .gap { height: 5px; }

  .website {
    position: absolute;
    left: 40px;
    bottom: 24px;
    font-family: "Open Sans", sans-serif;
    font-size: 13px;
    font-weight: 600;
    letter-spacing: 3px;
    color: var(--on-dark);
  }
</style>
</head>
<body>
<main class="sheet">

  <section class="card card--front" aria-label="Business card front">
    <svg class="card-art" viewBox="0 0 680 389" aria-hidden="true">
      <path d="M0,272 C220,272 400,230 500,150 C570,96 620,74 680,66 L680,389 L0,389 Z" fill="var(--swoosh-light)"/>
      <path d="M0,288 C220,288 405,246 505,166 C575,112 625,90 680,82 L680,389 L0,389 Z" fill="var(--swoosh-grey)"/>
      <path d="M0,300 C220,300 410,258 510,178 C580,124 630,102 680,94 L680,389 L0,389 Z" fill="var(--card-white)"/>
      <path d="M0,308 C220,308 414,266 514,186 C584,132 634,110 680,102 L680,389 L0,389 Z" fill="var(--charcoal)"/>
    </svg>

    <div class="brand"><span class="brand-mark"></span>Dalworth Pryce</div>

    <div class="person">
      <p class="person-name">Marcus Hale</p>
      <p class="person-title">Owner / C.E.O</p>
    </div>

    <ul class="contact">
      <li>4180 Brambleton Lane, Suite 310<span class="icon"></span></li>
      <li>Houston, TX 77051<span class="icon icon--blank"></span></li>
      <li class="gap"></li>
      <li>713-508-9627<span class="icon"></span></li>
      <li>281-369-0714<span class="icon icon--blank"></span></li>
      <li>832-415-7703<span class="icon icon--blank"></span></li>
      <li class="gap"></li>
      <li>marcus@dalworthpryce.com<span class="icon"></span></li>
      <li>www.dalworthpryce.com<span class="icon"></span></li>
    </ul>
  </section>

  <section class="card card--back" aria-label="Business card back">
    <svg class="card-art" viewBox="0 0 680 389" aria-hidden="true">
      <path d="M0,150 C160,158 300,246 450,298 C540,328 620,338 680,338 L680,389 L0,389 Z" fill="var(--swoosh-light)"/>
      <path d="M0,166 C160,174 300,262 450,314 C540,344 620,353 680,353 L680,389 L0,389 Z" fill="var(--swoosh-grey)"/>
      <path d="M0,178 C160,186 300,274 450,326 C540,356 620,364 680,364 L680,389 L0,389 Z" fill="var(--card-white)"/>
      <path d="M0,186 C160,194 300,282 450,334 C540,363 620,371 680,371 L680,389 L0,389 Z" fill="var(--charcoal)"/>
    </svg>

    <div class="brand"><span class="brand-mark"></span>Dalworth Pryce</div>

    <div class="website">www.dalworthpryce.com</div>
  </section>

</main>
</body>
</html>
```